Modern business card design for professional copywriter

I'd like a business card design that I can use to have my cards printed out by tavrel.com as a squared corners business card (see artwork and design guidelines here: https://help.tavrel.com/hc/en-gb/sections/300481762-TAVREL-Product-Templates)

The design should be clean and modern and reflect the colours, tone and branding on my website: https://gretafolvane.com.au

Target Market(s)

Professionals, B2B small business owners

Industry/Entity Type

Business

Contact Information for Business Card

Greta Folvane
m: 0427 954 368
e: greta@gretafolvane.com.au
w: gretafolvane.com.au

Font styles to use
Sans Serif

Requirements
Must have
• Tagline: "Smart copywriting for clever business people"
• Brand colours: fd8000, 009984, 666666 and black
Nice to have

```html
<!DOCTYPE html>
<html lang="en">
<head>
<meta charset="utf-8">
<title>Greta Folvane – Business Card</title>
<link href="https://fonts.googleapis.com/css2?family=Questrial&family=Arimo:wght@400&display=swap" rel="stylesheet">
<style>
  :root {
    --orange: #f5861f;
    --teal: #179c84;
    --grey: #666666;
    --backdrop: #525252;
    --card: #ffffff;
    --ink: #111111;
    --chip: #dadade;
    --chip-text: #555555;
    --body-text: #444444;
  }
  html, body {
    margin: 0;
    padding: 0;
    width: 1200px;
    height: 1200px;
    overflow: hidden;
    background: var(--backdrop);
  }
  .canvas { position: relative; width: 1200px; height: 1200px; }
  .card {
    position: absolute;
    left: 266px;
    width: 672px;
    height: 440px;
    background: var(--card);
    overflow: hidden;
  }
  .card--front { top: 127px; }
  .card--back { top: 630px; }

  .identity {
    position: absolute;
    right: 316px;
    top: 290px;
    text-align: right;
    color: var(--ink);
    font-family: "Questrial", sans-serif;
  }
  .card--front .identity { top: 163px; }
  .identity__name { font-size: 44px; line-height: 1; letter-spacing: 1px; margin: 0; }
  .identity__role { font-size: 24px; line-height: 1; letter-spacing: 1px; margin: 8px 0 0; }

  .portrait { position: absolute; left: 397px; top: 106px; width: 198px; height: 198px; }

  .tagline {
    position: absolute;
    left: 0; right: 0;
    top: 375px;
    text-align: center;
    font-family: "Arimo", sans-serif;
    font-size: 23px;
    color: var(--ink);
    margin: 0;
  }

  .ring-back { position: absolute; left: 0; top: 0; width: 672px; height: 440px; }
  .pitch {
    position: absolute;
    left: 26px;
    top: 281px;
    width: 180px;
    font-family: "Arimo", sans-serif;
    font-size: 12px;
    line-height: 14.3px;
    color: var(--body-text);
  }
  .pitch p { margin: 0 0 14px; }

  .contacts { position: absolute; left: 331px; top: 121px; }
  .contact { display: flex; height: 55px; margin-bottom: 13px; }
  .contact__icon {
    width: 55px; height: 55px;
    display: flex; align-items: center; justify-content: center;
  }
  .contact__icon--teal { background: var(--teal); }
  .contact__icon--orange { background: var(--orange); }
  .contact__value {
    margin-left: 7px;
    width: 196px;
    padding-left: 14px;
    background: var(--chip);
    display: flex; align-items: center;
    font-family: "Questrial", sans-serif;
    font-size: 15px;
    color: var(--chip-text);
  }
  .contact__value--phone { font-size: 16px; letter-spacing: 1.5px; padding-left: 17px; }
  .contact__value--email { padding-left: 11px; }
</style>
</head>
<body>
<div class="canvas">

  <section class="card card--front">
    <div class="identity">
      <h1 class="identity__name">Greta Folvane</h1>
      <p class="identity__role">COPYWRITER</p>
    </div>

    <svg class="portrait" viewBox="0 0 198 198">
      <defs>
        <radialGradient id="portrait-tone" cx="50%" cy="40%" r="60%">
          <stop offset="0" stop-color="#e6d6c4"/>
          <stop offset="0.6" stop-color="#d9dadb"/>
          <stop offset="1" stop-color="#8a8a86"/>
        </radialGradient>
      </defs>
      <path d="M99 6 A93 93 0 0 1 192 99" fill="none" stroke="var(--teal)" stroke-width="13"/>
      <path d="M192 99 A93 93 0 0 1 99 192" fill="none" stroke="var(--orange)" stroke-width="13"/>
      <path d="M99 192 A93 93 0 0 1 6 99" fill="none" stroke="var(--teal)" stroke-width="13"/>
      <path d="M6 99 A93 93 0 0 1 99 6" fill="none" stroke="var(--orange)" stroke-width="13"/>
      <circle cx="99" cy="99" r="85" fill="url(#portrait-tone)" role="img" aria-label="Portrait photo of the copywriter"/>
    </svg>

    <p class="tagline">Smart copywriting for clever business people</p>
  </section>

  <section class="card card--back">
    <svg class="ring-back" viewBox="0 0 672 440">
      <path d="M91 198 A145 145 0 0 1 236 350" fill="none" stroke="var(--grey)" stroke-width="14"/>
      <path d="M236 350 A145 145 0 0 1 91 495" fill="none" stroke="var(--teal)" stroke-width="14"/>
      <path d="M-54 350 A145 145 0 0 1 91 198" fill="none" stroke="var(--orange)" stroke-width="14"/>
    </svg>
    <div class="pitch">
      <p>f you’re concerned that a copywriter won’t understand the complexities or nuances of your work, talk to me.</p>
      <p>I love working with clients who do clever things.</p>
    </div>

    <div class="contacts">
      <div class="contact">
        <div class="contact__icon contact__icon--teal">
          <svg width="30" height="30" viewBox="0 0 24 24" aria-hidden="true">
            <path fill="#fff" d="M6.6 10.8c1.4 2.8 3.8 5.1 6.6 6.6l2.2-2.2c.3-.3.7-.4 1-.2 1.1.4 2.3.6 3.6.6.6 0 1 .4 1 1V20c0 .6-.4 1-1 1C10.6 21 3 13.4 3 4c0-.6.4-1 1-1h3.5c.6 0 1 .4 1 1 0 1.3.2 2.5.6 3.6.1.3 0 .7-.2 1z"/>
          </svg>
        </div>
        <div class="contact__value contact__value--phone">0427 954 368</div>
      </div>
      <div class="contact">
        <div class="contact__icon contact__icon--orange">
          <svg width="32" height="32" viewBox="0 0 32 32" aria-hidden="true" fill="none" stroke="#fff" stroke-width="2">
            <circle cx="16" cy="16" r="13"/>
            <ellipse cx="16" cy="16" rx="6" ry="13"/>
            <line x1="16" y1="3" x2="16" y2="29"/>
            <line x1="3" y1="16" x2="29" y2="16"/>
            <line x1="5" y1="10" x2="27" y2="10"/>
            <line x1="5" y1="22" x2="27" y2="22"/>
          </svg>
        </div>
        <div class="contact__value">gretafolvane.com.au</div>
      </div>
      <div class="contact">
        <div class="contact__icon contact__icon--teal">
          <svg width="32" height="22" viewBox="0 0 32 22" aria-hidden="true" fill="none" stroke="#fff" stroke-width="1.6">
            <rect x="1" y="1" width="30" height="20" fill="#fff"/>
            <path d="M1 1 L16 13 L31 1 M1 21 L12 10 M31 21 L20 10" stroke="var(--teal)"/>
          </svg>
        </div>
        <div class="contact__value contact__value--email">greta@gretafolvane.com.au</div>
      </div>
    </div>
  </section>

</div>
</body>
</html>
```